Flyer-Design für eine Therapeutin
Zielgruppe
Ich bin Therapeutin und biete u.a. Massagen, Craniosacrale Integration, LebensenergieBeratung usw. an
Die Zielgruppe sind gesundheitsbewusste, selbstreflektierte Frauen und Männer mittleren Alters.
Aufgabenstellung
Ich stelle mir einen Wickelfalz Flyer in üblichem DIN A 4 Format vor, bin aber auch offen für Neues. Die Farben hätte ich gerne in grün, türkis, blau und lila/aubergine.

```html
<!DOCTYPE html>
<html lang="de">
<head>
<meta charset="utf-8">
<title>Wickelfalz-Flyer – Hof Lindenau</title>
<link href="https://fonts.googleapis.com/css2?family=Lato:wght@400;700;900&family=Parisienne&display=swap" rel="stylesheet">
<style>
  :root {
    --backdrop: #eaf0f7;
    --paper: #ffffff;
    --paper-shade: #f6f7f8;
    --fold: #e3e6ea;
    --wave-blue: #2b6cb5;
    --wave-light: #d6e6f7;
    --ink: #1f2226;
    --photo-warm: #7a4a2c;
    --photo-cool: #2f5f7c;
  }
  * { box-sizing: border-box; margin: 0; padding: 0; }
  html, body {
    width: 1200px; height: 900px; overflow: hidden;
    background: var(--backdrop);
  }
  .flyer {
    position: absolute; left: 30px; top: 47px;
    width: 1140px; height: 806px;
    background: var(--paper);
    box-shadow: 0 10px 30px rgba(40, 70, 110, 0.15);
    font-family: "Lato", sans-serif;
    color: var(--ink);
  }
  .flyer-art { position: absolute; inset: 0; width: 1140px; height: 806px; }
  .panel { position: absolute; top: 0; width: 380px; height: 806px; }
  .panel--offers { left: 0; background: linear-gradient(180deg, var(--paper), var(--paper-shade)); }
  .panel--contact { left: 380px; }
  .panel--cover { left: 760px; }
  .script {
    font-family: "Parisienne", cursive;
    font-weight: 400;
    text-align: center;
    line-height: 1.05;
  }
  .offers-intro { position: absolute; top: 196px; left: 20px; right: 20px; font-size: 27px; }
  .offers-list {
    position: absolute; top: 272px; left: 0; right: 0;
    list-style: none; text-align: center;
    font-size: 16px; line-height: 21px;
  }
  .booking-call { position: absolute; top: 52px; left: 0; right: 0; font-size: 34px; }
  .booking-phone {
    position: absolute; top: 140px; left: 0; right: 0;
    text-align: center; font-size: 40px; font-weight: 900;
    color: var(--wave-blue); letter-spacing: 0.5px;
  }
  .address { position: absolute; top: 352px; left: 0; right: 0; text-align: center; font-size: 17px; line-height: 21px; }
  .address-name { font-weight: 700; }
  .web { position: absolute; top: 462px; left: 0; right: 0; text-align: center; font-size: 16px; line-height: 21px; }
  .brand {
    position: absolute; top: 52px; left: 22px;
    display: flex; align-items: center; gap: 8px;
    font-size: 19px; font-weight: 700; color: var(--ink);
  }
  .brand-dot { width: 14px; height: 14px; border-radius: 50%; background: var(--wave-blue); }
  .cover-slogan { position: absolute; top: 690px; left: 110px; right: 20px; font-size: 36px; }
</style>
</head>
<body>
  <main class="flyer">
    <section class="panel panel--offers"></section>
    <section class="panel panel--contact"></section>
    <section class="panel panel--cover"></section>

    <svg class="flyer-art" viewBox="0 0 1140 806" aria-hidden="false">
      <defs>
        <linearGradient id="portraitTone" x1="0" y1="0" x2="0.6" y2="1">
          <stop offset="0" stop-color="#b7a08c"/>
          <stop offset="0.45" stop-color="var(--photo-warm)"/>
          <stop offset="1" stop-color="var(--photo-cool)"/>
        </linearGradient>
      </defs>
      <!-- folds -->
      <line x1="380" y1="0" x2="380" y2="806" stroke="var(--fold)" stroke-width="1.5"/>
      <line x1="760" y1="0" x2="760" y2="806" stroke="var(--fold)" stroke-width="1.5"/>
      <!-- light waves -->
      <path d="M0,150 C70,120 130,105 200,115 C270,125 330,185 380,215 C450,262 520,302 600,298 C680,294 730,282 760,270 C800,255 815,215 845,200 C900,176 1000,166 1140,210"
            fill="none" stroke="var(--wave-light)" stroke-width="26"/>
      <path d="M760,610 C900,650 1060,640 1140,600 L1140,640 C1000,650 880,670 760,690 Z" fill="var(--wave-light)"/>
      <path d="M420,785 C470,650 600,560 760,520 C880,492 990,470 1140,470" fill="none" stroke="var(--wave-light)" stroke-width="12"/>
      <!-- portrait area -->
      <path role="img" aria-label="Porträtfoto der Therapeutin"
            d="M760,282 C790,258 812,222 842,207 C895,182 985,166 1140,215 L1140,600 C1060,640 900,650 760,610 Z"
            fill="url(#portraitTone)"/>
      <!-- blue waves -->
      <path d="M0,115 C50,95 110,72 180,85 C260,100 320,170 380,205 C450,250 520,290 600,285 C680,280 730,265 760,255 C800,240 815,200 845,185 C900,160 1000,150 1140,195"
            fill="none" stroke="var(--wave-blue)" stroke-width="16" stroke-linecap="butt"/>
      <path d="M0,668 C120,622 260,618 380,680 C480,728 620,720 760,690 C880,664 1000,640 1140,628"
            fill="none" stroke="var(--wave-blue)" stroke-width="5"/>
    </svg>

    <div class="panel panel--offers">
      <p class="script offers-intro">Fühle Dich tief berührt mit meinen wohltuenden Angeboten:</p>
      <ul class="offers-list">
        <li>Massagen</li>
        <li>CranioSacrale Integration</li>
        <li>SomatoEmotionale Entspannung</li>
        <li>Herzzentrierte Therapie</li>
        <li>RessourcenBox</li>
        <li>LebensenergieBeratung</li>
        <li>Meditationen</li>
        <li>WorkIn</li>
        <li>Präventive Physiotherapie</li>
        <li>PräventionsTraining</li>
      </ul>
    </div>

    <div class="panel panel--contact">
      <p class="script booking-call">Jetzt Termin<br>vereinbaren unter</p>
      <p class="booking-phone">0160-5550123</p>
      <address class="address" style="font-style: normal;">
        <span class="address-name">Lena Wiesberger</span><br>
        Lindenweg 7<br>
        94000 Musterau
      </address>
      <p class="web">kontakt@hoflindenau-beispiel.de<br>www.hoflindenau-beispiel.de</p>
    </div>

    <div class="panel panel--cover">
      <div class="brand"><span class="brand-dot"></span>Hof Lindenau</div>
      <p class="script cover-slogan">Fühl Dich tief<br>berührt!</p>
    </div>
  </main>
</body>
</html>
```